Oil and Gas Letterhead Design Tweak

Simple letterhead information and design tweak.

Please note, we don't want to change the design or logo of the letterhead only the small changes mentioned below.

We need to change the company name up top to "Northvale Petrotech Kestra"

Also, we need to include in the footer the following information. I have attached an image of roughly how we would like to have it displayed in the footer.

Footer Details:

Northvale Petrotech Kestra,
Unit No. 7283, Kestra Business Center, level No. 2, R&P 8, Dubai, United Arab Emirates
Northvale Petrotech Kestra is registered as a free zone company under the rules & regulations of Kestra

Target Market(s)

O&G Market

Industry/Entity Type

Oil And Gas

Font styles to use
Sans Serif

Colors

Designer to choose colors to be used in the design.

Requirements
Must have
• Change the company name to Northvale Petrotech Kestra
• Include the footer on the bottom of the first and continuation page
Should not have
• Should not change the design or logo of the letterhead, only the specified changes mentioned above

```html
<!DOCTYPE html>
<html lang="en">
<head>
<meta charset="utf-8">
<title>Northvale Petrotech Kestra – Letterhead</title>
<link rel="stylesheet" href="https://fonts.googleapis.com/css2?family=Source+Sans+3:wght@400;500&display=swap">
<style>
  :root {
    --brand-blue: #1f5fae;
    --brand-red: #e3242b;
    --ink-navy: #1e2a55;
    --ink-text: #1a1a1a;
    --paper: #ffffff;
  }
  * { margin: 0; padding: 0; box-sizing: border-box; }
  html, body {
    width: 848px;
    height: 1200px;
    overflow: hidden;
    background: var(--paper);
  }
  .letterhead {
    position: relative;
    width: 848px;
    height: 1200px;
    background: var(--paper);
    font-family: "Source Sans 3", sans-serif;
    overflow: hidden;
  }
  .top-bands, .corner-tabs {
    position: absolute;
    display: block;
  }
  .top-bands { left: 0; top: 0; }
  .corner-tabs { left: 600px; top: 1170px; }
  .band-blue, .tab-blue { fill: var(--brand-blue); }
  .band-red, .tab-red { fill: var(--brand-red); }

  .company-name {
    position: absolute;
    left: 270px;
    top: 50px;
    font-size: 26px;
    font-weight: 500;
    color: var(--ink-navy);
    letter-spacing: 0.1px;
    white-space: nowrap;
  }

  .footer-details {
    position: absolute;
    left: 131px;
    top: 978px;
    font-size: 14px;
    line-height: 18.5px;
    color: var(--ink-text);
    font-weight: 500;
  }
  .footer-details p { white-space: nowrap; }
</style>
</head>
<body>
  <div class="letterhead">
    <svg class="top-bands" width="848" height="16" viewBox="0 0 848 16" aria-hidden="true">
      <polygon class="band-blue" points="0,0 196,0 186,14 0,14"/>
      <polygon class="band-red" points="224,0 848,0 848,14 214,14"/>
    </svg>

    <h1 class="company-name">Northvale Petrotech Kestra</h1>

    <footer class="footer-details">
      <p>Unit No. 7283 | Kestra Business Center | level No. 2, R&amp;P 8 |</p>
      <p>Dubai | United Arab Emirates</p>
      <p>Northvale Petrotech Kestra is registered as a free zone</p>
      <p>company under the rules &amp; regulations of Kestra</p>
    </footer>

    <svg class="corner-tabs" width="110" height="22" viewBox="0 0 110 22" aria-hidden="true">
      <polygon class="tab-blue" points="22,6 60,6 54,20 14,20"/>
      <polygon class="tab-red" points="68,6 106,6 106,20 62,20"/>
    </svg>
  </div>
</body>
</html>
```